Grumpy mite pest control logo and banner

We need a banner design and logo for a new pest control company based out of Phoenix Arizona. We do general pest control along with weeding and termites. etc The company name is changing from Pinecrest Pest control to Grumpy Mite Pest Control. Our website will have animated cartoon-like bug characters and we are wanting something to coincide. Cartoon-like images similar to The Odd Porch comics or the movie A Beetle's Tale and the comic Crawlby (crawlbystrip.example). We have in mind some funny cartoons where the bugs are bigger than life, as big or bigger than humans with very exaggerated features. One idea was a cartoon with a woman lying in bed sleeping and a bed bug bigger than her hovering over her with a napkin and fork and spoon like he was getting ready to eat her.
We are wanting the backdrop to possibly be black and red or orange and white like is on our website currently. The company website is www.pinecrestpest.example .
Our catch phrase needs to be on the banner: no grumpy paperwork.
We will be using this banner at trade shows to market our business.
Updates

Industry/Entity Type

Pest Control

Requirements
Must have
• Company Name: Grumpy Mite Pest Control
• Catch Phrase: No Grumpy Paperwork
• Phone: 602-555-0148
• We are wanting bullet points of main services:
• Bees, wasp, bed bugs, scorpions, spiders olive tress, turf & ornamental, soil testing, rodents.....
• Our services are listed at http://pinecrestpest.example/services.php
• We would like animated cartoon-like characters similar to the Valemont cartoon A Beetle's Tale and the comic strips Crawlby and The Odd Porch.
Nice to have
• I would like simple sketches next to each of the services. Whiteboard sketch style. something funny to go along with the type of bug/service it is.

```html
<!DOCTYPE html>
<html lang="en">
<head>
<meta charset="utf-8">
<title>Grumpy Mite Pest Control – Logo and Banner</title>
<link rel="stylesheet" href="https://fonts.googleapis.com/css2?family=Ribeye&family=Roboto+Condensed:wght@400&family=Open+Sans:wght@400&display=swap">
<style>
  :root {
    --paper: #ffffff;
    --ink: #000000;
    --bug-orange: #f47b20;
    --alert-red: #ed1c24;
    --panel-black: #000000;
    --reverse-white: #ffffff;
  }
  * { box-sizing: border-box; margin: 0; padding: 0; }
  html, body { width: 1200px; height: 1200px; overflow: hidden; background: var(--paper); }
  .canvas { position: relative; width: 1200px; height: 1200px; background: var(--paper); }

  .brand-lockup { position: absolute; left: 0; width: 1200px; display: flex; flex-direction: column; align-items: center; }
  .brand-name {
    font-family: "Ribeye", cursive;
    font-size: 62px;
    line-height: 1;
    white-space: nowrap;
  }
  .tagline-row { display: flex; align-items: center; gap: 10px; margin-top: 22px; }
  .tagline-rules { display: block; }
  .tagline {
    font-family: "Open Sans", sans-serif;
    font-size: 38px;
    letter-spacing: 3px;
    line-height: 1;
  }

  /* light version */
  .lockup-light { top: 205px; }
  .lockup-light .brand-name { color: var(--ink); }
  .lockup-light .tagline { color: var(--ink); }

  .call-stack { position: absolute; top: 395px; left: 0; width: 1200px; text-align: center; color: var(--alert-red); font-family: "Ribeye", cursive; }
  .call-label { font-size: 42px; letter-spacing: 2px; line-height: 1; }
  .call-number { font-size: 86px; letter-spacing: 6px; line-height: 1; margin-top: 28px; }

  /* dark version */
  .dark-panel { position: absolute; left: 28px; top: 628px; width: 1148px; height: 540px; background: var(--panel-black); }
  .lockup-dark { top: 830px; }
  .lockup-dark .brand-name { color: var(--alert-red); }
  .lockup-dark .tagline { color: var(--alert-red); }

  .call-line {
    position: absolute; top: 1070px; left: 0; width: 1200px; text-align: center;
    font-family: "Ribeye", cursive; font-size: 62px; letter-spacing: 4px; line-height: 1;
    color: var(--reverse-white); white-space: nowrap;
  }
</style>
</head>
<body>
<main class="canvas">

  <section class="brand-lockup lockup-light">
    <h1 class="brand-name">Grumpy Mite Pest Control</h1>
    <div class="tagline-row">
      <svg class="tagline-rules" width="356" height="22" viewBox="0 0 356 22" aria-hidden="true">
        <rect x="0" y="2" width="356" height="6" fill="var(--ink)"/>
        <rect x="0" y="14" width="356" height="6" fill="var(--bug-orange)"/>
      </svg>
      <p class="tagline">no grumpy paperwork</p>
    </div>
  </section>

  <section class="call-stack">
    <p class="call-label">CALL US NOW</p>
    <p class="call-number">602-555-0148</p>
  </section>

  <section class="dark-panel" aria-label="Reversed banner"></section>

  <section class="brand-lockup lockup-dark">
    <h2 class="brand-name">Grumpy Mite Pest Control</h2>
    <div class="tagline-row">
      <svg class="tagline-rules" width="356" height="22" viewBox="0 0 356 22" aria-hidden="true">
        <rect x="0" y="2" width="356" height="6" fill="var(--alert-red)"/>
        <rect x="0" y="14" width="356" height="6" fill="var(--bug-orange)"/>
      </svg>
      <p class="tagline">no grumpy paperwork</p>
    </div>
  </section>

  <p class="call-line">CALL US NOW 602-555-0148</p>

</main>
</body>
</html>
```